依頼詳細
商品や価格帯を口頭でしか伝えられてないので、チラシでこんな感じのものでどのくらいの価格帯かを伝えるチラシを作っていただきたいです。
記載項目
●社名:Whistling Meadow(ホイッスリング メドウ)
●電話番号:072-555-0148
●mail:whistling.meadow@mailqorvex.com
●URL:http://w-meadow-qorvex.com/
●料金プラン:
お祝い・記念日・誕生日など様々なシーンに!
バルーンアレンジメント・・\5,000~

結婚式・開店祝いなどメッセージカードをつけて!
バルーンブーケ・・・・・・\5,000~

フラワースタンドを圧倒するインパクト!
バルーンスタンド・・・・・\25,000~

各種イベントの演出に!
バルーンアーチ・・・・・・\40,000~

季節のデコレーションからプロポーズ演出まで!
バルーンデコレーション・・\50,000~

●キャッチコピー:To create a dream and smile
●ロゴ:添付ファイル
●商品写真:添付ファイル
●発送:大阪北摂エリア無料配達いたします。【バルーンギフト・ブーケは全国発送可能※一部離島を除く】
●ご予算・ご希望に応じてオリジナルでお作り致します。
作り置きはしておりません。在庫に限りがございますので、お早目のご予約をおすすめいたします。
どんなことでもお気軽にご相談下さい。
サイズ
A4
ページ数
片面
希望イメージ
シンプル 複雑
単色 カラフル
暗い 明るい
日常 高級
遊び心 厳粛
未来的 伝統的
女性的 男性的
希望する色
ロゴデザインがポップで、カラーがオレンジですが、あまり安っぽくない感じの色目でお願いします。
納品ファイル
• 高解像度JPG (.jpg)
• イラストレーター形式 (.ai)
• フォトショップ形式 (.psd)
• PNG形式 (.png)
補足説明
参考にサンプルチラシを添付します。
添付データ漏れていたのでアップします。
画象1点追加しました。(バルーンアレンジメント02)
■ 選んだ理由

たくさんの提案の中、本当に悩みに悩んで決めさせていただきました。
社員ともども色使いが落ち着いている中で上品に仕上げてくれている点を気に入り今回選ばせていただきました。

■ 提案者全員のお礼・コメント

このたびはたくさんのご提案をありがとうございました。
本当に素晴らしい作品ばかりで、悩みに悩み、決めるのに時間がかかり申し訳ございませんでした。
また、今後も色々とハコニワークを利用していきますので、またの機会によろしくお願いいたします。
本当にありがとうございました。

```html
<!DOCTYPE html>
<html lang="ja">
<head>
<meta charset="utf-8">
<title>Whistling Meadow バルーン料金プラン</title>
<link rel="stylesheet" href="https://fonts.googleapis.com/css2?family=M+PLUS+Rounded+1c:wght@400;700;800&family=Pacifico&family=Dancing+Script:wght@700&display=swap">
<style>
:root{
  --bg-deep:#062a31;
  --bg-teal:#0f4a52;
  --pink:#ff6fa8;
  --pink-soft:#ffb3cf;
  --yellow:#ffd83a;
  --green:#8cc63f;
  --orange:#f08a1c;
  --white:#ffffff;
  --ink:#333333;
}
*{box-sizing:border-box;margin:0;padding:0}
html,body{width:849px;height:1200px;overflow:hidden}
body{font-family:"M PLUS Rounded 1c",sans-serif;background:var(--bg-deep)}
.flyer{position:relative;width:849px;height:1200px;overflow:hidden;
  background:radial-gradient(ellipse at 60% 35%,var(--bg-teal) 0%,var(--bg-deep) 70%)}
.photo{position:absolute;border-radius:6px}
.photo-arrangement-a{left:14px;top:14px;width:214px;height:156px;background:linear-gradient(135deg,#d9d2e6,#b07ab6 55%,#6b2f74)}
.photo-arrangement-b{left:14px;top:182px;width:214px;height:186px;background:linear-gradient(160deg,#2b6a3a,#e86a9a 50%,#b81f52)}
.photo-stand{left:430px;top:120px;width:300px;height:700px;border-radius:40px;
  background:radial-gradient(ellipse at 50% 20%,#ff2a4a 0%,#d8115c 30%,transparent 60%),radial-gradient(ellipse at 50% 70%,#f59ad0 0%,#8e58c8 30%,transparent 55%),linear-gradient(180deg,#1d5a60,#0b3a40)}
.photo-arch{left:330px;top:820px;width:270px;height:282px;background:radial-gradient(ellipse at 50% 60%,#2d6d3a 0%,#1b3e5a 40%,#c03058 70%,#0d2f38 100%)}
.photo-bouquet{left:608px;top:640px;width:228px;height:462px;background:radial-gradient(ellipse at 50% 30%,#d2102c 0%,#8a0c1c 35%,#1a1a1a 60%,#0b3a40 100%)}
.photo-decoration{left:14px;top:935px;width:190px;height:167px;background:linear-gradient(160deg,#e9f3e0,#7fc06a 50%,#2f6f35)}
.headline{position:absolute;left:396px;top:20px;width:440px;text-align:right;color:var(--pink-soft)}
.headline .lead{font-size:23px;font-weight:700;letter-spacing:1px}
.headline .main{font-size:34px;font-weight:800;color:var(--pink);margin-top:4px}
.badge{position:absolute;text-align:center;color:var(--white);white-space:nowrap}
.badge .num{display:block;margin:0 auto;width:52px;height:52px;border-radius:50%;background:var(--green);
  border:3px solid var(--white);font-size:30px;font-weight:800;line-height:46px}
.badge .name{display:block;font-size:20px;font-weight:800;margin-top:4px;text-shadow:0 1px 3px rgba(0,0,0,.6)}
.badge .price{display:block;font-size:13px;font-weight:700}
.badge-1{left:235px;top:110px;width:160px}
.badge-3{left:724px;top:400px;width:110px}
.badge-4{left:520px;top:800px;width:120px}
.badge-2{left:700px;top:990px;width:120px}
.badge-5{left:180px;top:960px;width:150px}
.intro{position:absolute;left:20px;top:420px;width:400px;color:var(--white)}
.intro .title{font-family:"Pacifico",cursive;font-size:58px;color:var(--yellow);line-height:1.1}
.intro .title small{font-family:"M PLUS Rounded 1c",sans-serif;font-size:20px;color:var(--yellow);font-weight:700;margin-left:8px}
.intro .tagline{font-family:"Dancing Script",cursive;font-size:26px;color:var(--yellow);margin-top:4px}
.intro .note{font-size:12px;margin-top:6px}
.plans{list-style:none;margin-top:14px}
.plans li{display:grid;grid-template-columns:28px 1fr;column-gap:8px;margin-bottom:12px}
.plans .n{width:24px;height:24px;border-radius:50%;background:var(--green);color:var(--white);font-weight:800;font-size:14px;text-align:center;line-height:24px;grid-row:span 2}
.plans .scene{font-size:12px;color:#cfe6e3}
.plans .item{font-size:16px;font-weight:700;color:var(--white);white-space:nowrap}
.plans .item b{color:var(--yellow)}
.footer{position:absolute;left:0;top:1108px;width:849px;height:92px;background:var(--white);display:flex;align-items:center;padding:0 14px;gap:12px}
.delivery{flex:none;width:176px;height:76px;border:3px solid var(--orange);border-radius:6px;text-align:center;color:var(--orange);padding-top:4px}
.delivery .big{font-size:21px;font-weight:800;line-height:1.15}
.delivery .small{font-size:9px;color:var(--ink);white-space:nowrap}
.brand{flex:none;display:flex;align-items:center;gap:8px;width:228px;white-space:nowrap}
.brand .dot{flex:none;width:34px;height:34px;border-radius:50%;background:var(--orange)}
.brand .name{font-size:19px;font-weight:800;color:var(--orange)}
.brand .sub{font-size:9px;color:var(--ink)}
.contact{flex:1;min-width:0;color:var(--ink);font-size:10.5px;white-space:nowrap}
.contact .tel{display:flex;align-items:center;gap:6px;font-size:27px;font-weight:800;color:var(--orange)}
.search{flex:none;display:flex;align-items:center;justify-content:space-between;width:140px;height:30px;border:2px solid #999;border-radius:4px;padding:0 6px;font-size:10px;color:var(--ink);align-self:flex-end;margin-bottom:10px;white-space:nowrap}
</style>
</head>
<body>
<main class="flyer">
  <div class="photo photo-arrangement-a" role="img" aria-label="バルーンアレンジメントの商品写真"></div>
  <div class="photo photo-arrangement-b" role="img" aria-label="誕生日向けバルーンアレンジメントの商品写真"></div>
  <div class="photo photo-stand" role="img" aria-label="ハート型バルーンとバタフライを組んだバルーンスタンドの写真"></div>
  <div class="photo photo-arch" role="img" aria-label="イベント用のバルーンアーチの写真"></div>
  <div class="photo photo-bouquet" role="img" aria-label="赤と黒のバルーンブーケの写真"></div>
  <div class="photo photo-decoration" role="img" aria-label="会場のバルーンデコレーションの写真"></div>

  <header class="headline">
    <p class="lead">お誕生日・発表会・結婚式・開店祝いに</p>
    <p class="main">華やかバルーンを！</p>
  </header>

  <div class="badge badge-1"><span class="num">1</span><span class="name">アレンジメント</span><span class="price">¥5,000〜</span></div>
  <div class="badge badge-3"><span class="num">3</span><span class="name">スタンド</span><span class="price">¥25,000〜</span></div>
  <div class="badge badge-4"><span class="num">4</span><span class="name">アーチ</span><span class="price">¥40,000〜</span></div>
  <div class="badge badge-2"><span class="num">2</span><span class="name">ブーケ</span><span class="price">¥5,000〜</span></div>
  <div class="badge badge-5"><span class="num">5</span><span class="name">デコレーション</span><span class="price">¥50,000〜</span></div>

  <section class="intro">
    <h1 class="title">Balloon<small>バルーン</small></h1>
    <p class="tagline">To Create a Dream and Smile</p>
    <p class="note">ご予算・ご希望に応じてオリジナルでお作り致します。</p>
    <ol class="plans">
      <li><span class="n">1</span><span class="scene">お祝い・記念日・誕生日など様々なシーンに！</span><span class="item">バルーンアレンジメント…<b>¥5,000〜</b></span></li>
      <li><span class="n">2</span><span class="scene">結婚式・開店祝いなどメッセージカードをつけて！</span><span class="item">バルーンブーケ……………<b>¥5,000〜</b></span></li>
      <li><span class="n">3</span><span class="scene">フラワースタンドを圧倒するインパクト！</span><span class="item">バルーンスタンド…………<b>¥25,000〜</b></span></li>
      <li><span class="n">4</span><span class="scene">各種イベントの演出に！</span><span class="item">バルーンアーチ……………<b>¥40,000〜</b></span></li>
      <li><span class="n">5</span><span class="scene">季節のデコレーションからプロポーズ演出まで！</span><span class="item">バルーンデコレーション…<b>¥50,000〜</b></span></li>
    </ol>
  </section>

  <footer class="footer">
    <div class="delivery">
      <p class="big">大阪北摂<br>無料配達</p>
      <p class="small">バルーンギフト・ブーケは全国発送可</p>
    </div>
    <div class="brand">
      <span class="dot"></span>
      <div><p class="name">Whistling Meadow</p><p class="sub">ホイッスリング メドウ</p></div>
    </div>
    <div class="contact">
      <p class="tel"><svg width="22" height="22" viewBox="0 0 24 24"><path fill="currentColor" d="M6.6 10.8a15 15 0 0 0 6.6 6.6l2.2-2.2c.3-.3.7-.4 1-.2 1.1.4 2.3.6 3.6.6.6 0 1 .4 1 1V20c0 .6-.4 1-1 1A17 17 0 0 1 3 4c0-.6.4-1 1-1h3.5c.6 0 1 .4 1 1 0 1.3.2 2.5.6 3.6.1.3 0 .7-.2 1z"/></svg>072-555-0148</p>
      <p>mail:whistling.meadow@mailqorvex.com</p>
      <p>URL:http://w-meadow-qorvex.com/</p>
    </div>
    <div class="search"><span>ホイッスリング メドウ</span><svg width="14" height="14" viewBox="0 0 24 24"><circle cx="10" cy="10" r="6" fill="none" stroke="#555" stroke-width="3"/><path d="M15 15l6 6" stroke="#555" stroke-width="3"/></svg></div>
  </footer>
</main>
</body>
</html>
```